Renata Quisby

Luxury And Style -

Black - White & Gold

Target Market(s)

Fashion

Industry/Entity Type

Fashion

Requirements
Must have
• High-End
Nice to have
• We will Print on Silk Paper

```html
<!DOCTYPE html>
<html lang="en">
<head>
<meta charset="utf-8">
<title>Renata Quisby — Letterhead</title>
<link rel="stylesheet" href="https://fonts.googleapis.com/css2?family=Source+Sans+3:wght@400;600&display=swap">
<style>
  :root {
    --backdrop: #acabab;
    --paper: #ffffff;
    --navy: #03031e;
    --gold: #c9a46a;
    --ink: #4a4a4a;
    --ink-strong: #3e3e3e;
    --white: #ffffff;
  }
  * { box-sizing: border-box; margin: 0; padding: 0; }
  html, body { width: 964px; height: 1200px; overflow: hidden; }
  body {
    background: var(--backdrop);
    font-family: "Source Sans 3", "Myriad Pro", Arial, sans-serif;
    position: relative;
  }
  .letterhead {
    position: absolute;
    left: 97px; top: 50px;
    width: 773px; height: 1093px;
    background: var(--paper);
  }
  .letterhead__band {
    position: absolute; left: 0; top: 0;
    width: 100%; height: 155px;
    background: var(--navy);
  }
  .brand {
    position: absolute; left: 50px; top: 66px;
    width: 220px;
    display: flex; align-items: center; justify-content: center; gap: 9px;
    font-family: "Source Sans 3", Arial, sans-serif;
    font-weight: 600; font-size: 19px;
    color: var(--gold);
  }
  .brand__dot { width: 9px; height: 9px; border-radius: 50%; background: var(--gold); flex: none; }
  .contact {
    position: absolute; left: 539px; top: 44px;
    color: var(--white); font-size: 12px; line-height: 15.5px; font-style: normal;
  }
  .contact__address { margin-bottom: 7px; }
  .contact__row { display: flex; align-items: center; gap: 9px; height: 16px; }
  .contact__row svg { width: 10px; height: 10px; fill: var(--gold); flex: none; }

  .letter { position: absolute; left: 73px; color: var(--ink); }
  .letter__date {
    top: 277px; font-size: 14.5px; font-weight: 600; color: var(--ink-strong);
  }
  .letter__recipient {
    top: 333px; font-size: 14.5px; font-weight: 600; line-height: 18.7px; color: var(--ink-strong);
  }
  .letter__body {
    top: 441px; width: 624px;
    font-size: 12.6px; line-height: 18.7px; letter-spacing: 0.1px;
    text-align: justify; hyphens: auto;
  }
  .letter__body p + p { margin-top: 18.7px; }

  .signature {
    position: absolute; left: 555px; top: 823px;
    width: 122px; height: 44px;
    background: linear-gradient(135deg, #f3f3f3, #e6e6e6);
  }
  .signature__title {
    position: absolute; left: 587px; top: 871px;
    font-size: 12.4px; color: var(--ink);
  }
</style>
</head>
<body>
  <main class="letterhead">
    <header class="letterhead__band">
      <div class="brand"><span class="brand__dot"></span>Renata Quisby</div>
      <address class="contact">
        <div class="contact__address">4870 Harbor Crest Ave<br>Palm Vale, FL 33990</div>
        <div class="contact__row">
          <svg viewBox="0 0 10 10" aria-hidden="true"><path d="M2 0.5 L3.6 0.5 L4.2 3 L3 3.8 C3.6 5.2 4.8 6.4 6.2 7 L7 5.8 L9.5 6.4 L9.5 8 C9.5 9 8.6 9.6 7.6 9.4 C4.4 8.8 1.2 5.6 0.6 2.4 C0.4 1.4 1 0.5 2 0.5 Z"/></svg>
          <span>555-018-2046</span>
        </div>
        <div class="contact__row">
          <svg viewBox="0 0 10 10" aria-hidden="true"><path d="M0.5 2 L9.5 2 L9.5 8.5 L0.5 8.5 Z M1.2 2.6 L5 5.6 L8.8 2.6" stroke="#03031e" stroke-width="0.8"/></svg>
          <span>hello@renataquisby.com</span>
        </div>
        <div class="contact__row">
          <svg viewBox="0 0 10 10" aria-hidden="true"><circle cx="5" cy="5" r="4.5"/><path d="M0.5 5 H9.5 M5 0.5 C2.8 3 2.8 7 5 9.5 M5 0.5 C7.2 3 7.2 7 5 9.5" stroke="#03031e" stroke-width="0.7" fill="none"/></svg>
          <span>www.renataquisby.com</span>
        </div>
      </address>
    </header>

    <p class="letter letter__date">Cartagena de Indias, Ocober 12,2015</p>

    <p class="letter letter__recipient">Sr.<br>TOMAS ELBRIDGE<br>Web Master<br>City</p>

    <section class="letter letter__body" lang="en">
      <p>Contrary to popular belief, Lorem Ipsum is not simply random text. It has roots in a piece of classical Latin literature from 45 BC, making it over 2000 years old. Edwin Harrowgate, a Latin professor at Bellmoor College in Vermont, looked up one of the more obscure Latin words, consectetur, from a Lorem Ipsum passage, and going through the cites of the word in classical literature,</p>
      <p>discovered the undoubtable source. Lorem Ipsum comes from sections 1.10.32 and 1.10.33 of "de Finibus Bonorum et Malorum" (The Extremes of Good and Evil) by Varro Lentus, written in 45 BC. This book is a treatise on the theory of ethics, very popular during the Renaissance. The first line of Lorem Ipsum, "Lorem ipsum dolor sit amet..", comes from a line in section 1.10.32.</p>
      <p>The standard chunk of Lorem Ipsum used since the 1500s is reproduced below for those interested. Sections 1.10.32 and 1.10.33 from "de Finibus Bonorum et Malorum" by Varro Lentus are also reproduced in their exact original form, accompanied by English versions from the 1914 translation by T. Marlowe.</p>
      <p>There are many variations of passages of Lorem Ipsum available, but the majority have suffered alteration in some form, by injected humour, or randomised words which don't look even slightly believable. If you are going to use a passage of Lorem Ipsum, you need to be sure there isn't anything embarrassing hidden in the middle of text. All the Lorem Ipsum generators o</p>
    </section>

    <div class="signature" role="img" aria-label="Handwritten signature of the founder"></div>
    <p class="signature__title">CEO/ FOUNDER</p>
  </main>
</body>
</html>
```